Banner Ad Design for Resume Builder Needed

For the ad copy and design of the ad, I leave that up to you. Keep in mind this is a do-it-yourself online resume builder. The site is simple to use and geared towards people who are unsure of how to write/create their own resume.

You can view the site (which isn't finished) and how it works at http://cvcrafter.demo.tplwerks.net/

I do not want the same color scheme or the logo used in the ad, just the most appealing ad for those looking to use a product like this

I need the ad in these sizes:

300x250, 728x90, 160x600, 468x60, 120x600, 300x100

```html
<!DOCTYPE html>
<html lang="en">
<head>
<meta charset="utf-8">
<title>Resume Builder Banner Set</title>
<link href="https://fonts.googleapis.com/css2?family=Oswald:wght@300;400&family=Open+Sans:wght@300;400;600;700&display=swap" rel="stylesheet">
<style>
  :root {
    --wood-dark: #3a1a0e;
    --wood-mid: #5e2b16;
    --wood-light: #7a3a1e;
    --red: #c8202a;
    --ink: #1e1e1e;
    --white: #ffffff;
    --link-blue: #1f6fb2;
    --strip-yellow: #f6eea0;
    --photo-light: #e9e4df;
    --photo-mid: #a9a29c;
    --photo-dark: #4a4440;
  }
  * { box-sizing: border-box; margin: 0; padding: 0; }
  html, body { width: 1200px; height: 857px; overflow: hidden; }
  body { font-family: "Open Sans", sans-serif; color: var(--ink); }

  .board {
    position: relative; width: 1200px; height: 857px; overflow: hidden;
    background: radial-gradient(ellipse at 50% 40%, var(--wood-light) 0%, var(--wood-mid) 45%, var(--wood-dark) 100%);
  }
  .sizes-title {
    position: absolute; left: 154px; top: 72px;
    font-weight: 300; font-size: 31px; color: var(--white); letter-spacing: 0.2px;
  }

  .banner { position: absolute; background: var(--white); overflow: hidden; }
  .photo { position: absolute; }
  .photo--office { background: linear-gradient(90deg, var(--photo-dark) 0%, var(--photo-mid) 45%, var(--photo-light) 100%); }
  .photo--person { background: linear-gradient(180deg, var(--photo-mid) 0%, var(--photo-light) 70%, var(--white) 100%); }

  .headline-condensed { font-family: "Oswald", sans-serif; font-weight: 400; color: var(--red); text-transform: uppercase; line-height: 1; }
  .cta { position: absolute; color: var(--white); font-weight: 700; text-transform: uppercase; text-align: center; line-height: 1.05; }
  .cta-shape { position: absolute; }

  /* 728x90 */
  .leaderboard { left: 215px; top: 177px; width: 624px; height: 77px; }
  .leaderboard .photo { left: 0; top: 0; width: 220px; height: 77px;
    background: linear-gradient(90deg, var(--photo-dark) 0%, var(--photo-mid) 60%, rgba(255,255,255,0) 100%); }
  .leaderboard .headline-condensed { position: absolute; left: 215px; top: 9px; font-size: 23px; font-weight: 300; }
  .leaderboard .body-copy { position: absolute; left: 215px; top: 35px; font-size: 13px; line-height: 15.5px; }
  .leaderboard .cta-shape { left: 464px; top: 0; width: 160px; height: 77px; }
  .leaderboard .cta { left: 485px; top: 27px; width: 139px; }
  .leaderboard .cta small { display: block; font-size: 11px; }
  .leaderboard .cta span { display: block; font-size: 16px; }

  /* 468x60 */
  .full-banner { left: 606px; top: 297px; width: 401px; height: 51px; }
  .full-banner .photo { left: 0; top: 0; width: 96px; height: 51px;
    background: linear-gradient(90deg, var(--photo-dark) 0%, var(--photo-mid) 70%, rgba(255,255,255,0) 100%); }
  .full-banner .headline-condensed { position: absolute; left: 106px; top: 6px; font-size: 15px; font-weight: 300; }
  .full-banner .body-copy { position: absolute; left: 106px; top: 24px; font-size: 9px; line-height: 10.5px; }
  .full-banner .cta-shape { left: 296px; top: 0; width: 105px; height: 51px; }
  .full-banner .cta { left: 310px; top: 18px; width: 91px; }
  .full-banner .cta small { display: block; font-size: 8px; }
  .full-banner .cta span { display: block; font-size: 11.5px; }

  /* skyscrapers */
  .skyscraper .photo { left: 0; top: 0; width: 100%; }
  .skyscraper .copy { position: absolute; left: 0; width: 100%; }
  .skyscraper .headline-condensed { text-align: center; }
  .skyscraper .pitch { text-transform: uppercase; font-weight: 400; color: var(--ink); }
  .skyscraper .pitch .lead { display: block; }
  .skyscraper .pitch .lead small { font-size: 0.6em; }
  .skyscraper .cta-shape { left: 0; width: 100%; }

  .skyscraper--narrow { left: 215px; top: 297px; width: 103px; height: 514px; }
  .skyscraper--narrow .photo { height: 176px; }
  .skyscraper--narrow .copy { top: 184px; }
  .skyscraper--narrow .headline-condensed { font-size: 38px; line-height: 32px; }
  .skyscraper--narrow .headline-condensed .big { font-size: 46px; line-height: 42px; display: block; }
  .skyscraper--narrow .pitch { padding: 0 0 0 6px; margin-top: 10px; font-size: 12.5px; line-height: 16px; }
  .skyscraper--narrow .pitch .lead { font-size: 19px; line-height: 17px; }
  .skyscraper--narrow .pitch .small-line { font-size: 11px; line-height: 12px; display: block; }
  .skyscraper--narrow .cta-shape { top: 442px; height: 72px; }
  .skyscraper--narrow .cta { left: 0; width: 100%; top: 468px; font-size: 12.5px; line-height: 16px; font-weight: 600; }

  .skyscraper--wide { left: 383px; top: 297px; width: 137px; height: 514px; }
  .skyscraper--wide .photo { height: 124px; }
  .skyscraper--wide .copy { top: 137px; }
  .skyscraper--wide .headline-condensed { font-size: 47px; line-height: 39px; }
  .skyscraper--wide .headline-condensed .big { font-size: 60px; line-height: 56px; display: block; }
  .skyscraper--wide .pitch { padding: 0 0 0 11px; margin-top: 8px; font-size: 16px; line-height: 19.5px; }
  .skyscraper--wide .pitch .lead { font-size: 23px; line-height: 21px; }
  .skyscraper--wide .pitch .small-line { font-size: 14px; line-height: 14px; display: block; }
  .skyscraper--wide .cta-shape { top: 428px; height: 86px; }
  .skyscraper--wide .cta { left: 0; width: 100%; top: 460px; font-size: 16px; line-height: 19px; font-weight: 600; }

  /* 300x250 */
  .rectangle { left: 606px; top: 399px; width: 257px; height: 214px; }
  .rectangle .photo { left: 0; top: 0; width: 235px; height: 190px;
    background: linear-gradient(90deg, var(--photo-dark) 0%, var(--photo-mid) 45%, var(--photo-light) 80%, rgba(255,255,255,0) 100%); }
  .rectangle .question { position: absolute; left: 122px; top: 10px; font-size: 17px; line-height: 19.5px; font-weight: 400; }
  .rectangle .question strong { display: block; color: var(--red); font-size: 26px; line-height: 28px; font-weight: 700; }
  .rectangle .site-url { position: absolute; left: 0; width: 100%; top: 192px; text-align: center; font-size: 12px; color: var(--link-blue); }

  /* 300x100 */
  .mobile-banner { left: 606px; top: 657px; width: 257px; height: 86px; }
  .mobile-banner .photo { left: 0; top: 0; width: 78px; height: 70px;
    background: linear-gradient(90deg, var(--photo-dark) 0%, var(--photo-mid) 60%, rgba(255,255,255,0) 100%); }
  .mobile-banner .question { position: absolute; left: 78px; top: 3px; font-size: 12.5px; line-height: 13px; }
  .mobile-banner .question strong { display: block; color: var(--red); font-size: 24px; line-height: 27px; font-weight: 700; }
  .mobile-banner .url-strip { position: absolute; left: 0; bottom: 0; width: 100%; height: 17px; background: var(--strip-yellow); }
  .mobile-banner .site-url { position: absolute; left: 27px; top: 1px; font-size: 12px; color: var(--ink); }
</style>
</head>
<body>
<main class="board" role="img" aria-label="Dark wood grain presentation background">
  <h1 class="sizes-title">300x250, 728x90, 160x600, 468x60, 120x600, 300x100</h1>

  <section class="banner leaderboard">
    <div class="photo" role="img" aria-label="Photo of two people pointing fists across a desk"></div>
    <h2 class="headline-condensed">No Writing Experience</h2>
    <p class="body-copy">Insert per written examples written by<br>resume writing experts for hundreds of jobs</p>
    <svg class="cta-shape" viewBox="0 0 160 77" preserveAspectRatio="none"><path d="M8 0 H160 V77 H8 Q32 38 8 0 Z" fill="var(--red)"/><path d="M0 0 Q24 38 0 77" fill="none" stroke="#e7b0b0" stroke-width="2"/></svg>
    <p class="cta"><small>Build your</small><span>Resume now</span></p>
  </section>

  <section class="banner full-banner">
    <div class="photo" role="img" aria-label="Photo of a stressed man at a laptop"></div>
    <h2 class="headline-condensed">No Writing Experience</h2>
    <p class="body-copy">Insert per written examples written by<br>resume writing experts for hundreds of jobs</p>
    <svg class="cta-shape" viewBox="0 0 105 51" preserveAspectRatio="none"><path d="M4 0 H105 V51 H4 Q18 25 4 0 Z" fill="var(--red)"/></svg>
    <p class="cta"><small>Build your</small><span>Resume now</span></p>
  </section>

  <section class="banner skyscraper skyscraper--narrow">
    <div class="photo photo--person" role="img" aria-label="Photo of a stressed man holding his head at a laptop"></div>
    <div class="copy">
      <h2 class="headline-condensed">Short<br>On<span class="big">Time?</span></h2>
      <p class="pitch"><span class="lead">Create <small>a</small></span><span class="small-line">Professional</span><span class="lead">Resume</span>In minutes<br>that will<br>separate you<br>from the<br>competition</p>
    </div>
    <svg class="cta-shape" viewBox="0 0 103 72" preserveAspectRatio="none"><path d="M0 14 Q51 -8 103 14 V72 H0 Z" fill="var(--red)"/></svg>
    <p class="cta">Build your<br>resume now</p>
  </section>

  <section class="banner skyscraper skyscraper--wide">
    <div class="photo photo--office" role="img" aria-label="Photo of two people pointing fists across a desk"></div>
    <div class="copy">
      <h2 class="headline-condensed">Short<br>On<span class="big">Time?</span></h2>
      <p class="pitch"><span class="lead">Create <small>a</small></span><span class="small-line">Professional</span><span class="lead">Resume</span>In minutes<br>that will<br>separate you<br>from the<br>competition</p>
    </div>
    <svg class="cta-shape" viewBox="0 0 137 86" preserveAspectRatio="none"><path d="M0 16 Q68 -10 137 16 V86 H0 Z" fill="var(--red)"/></svg>
    <p class="cta">Build your<br>resume now</p>
  </section>

  <section class="banner rectangle">
    <div class="photo" role="img" aria-label="Photo of a panicked woman holding a help sign beside a laptop"></div>
    <p class="question">Unsure of how<br>to write/create<br>their own<strong>RESUME</strong></p>
    <p class="site-url">www.cvcrafter.demo.tplwerks.net</p>
  </section>

  <section class="banner mobile-banner">
    <div class="photo" role="img" aria-label="Photo of a thoughtful young man"></div>
    <p class="question">Unsure of how to write/<br>create their own<strong>RESUME</strong></p>
    <div class="url-strip"><p class="site-url">www.cvcrafter.demo.tplwerks.net</p></div>
  </section>
</main>
</body>
</html>
```